Expense Tracker App for Young Adults

I need a mobile app designer to design an app UI for me. It is for an expense tracker app. I’ve attached a mind map of the various screens and features of the app.

I would like to see designs for this app which is targeted towards young adults (late teens & early 20s) just starting their career who want to plan their budgets and track their expenses.
Updates

Hello designers! I'm conscious that this is not a guaranteed project, so I can understand that some of you might be apprehensive. Just wanted to let you know that I'm willing to see your initial drafts that show your direction and theme for design. You don't have to design the whole app. In fact, it's better if you share your initial design ideas so that we can have a discussion and I can give my input. If I see some good initial designs, I will be happy to make this a guaranteed project. I'm simply being cautious since I'm bootstrapping this and funding out of my own pocket. Thank you for your understanding!

Target Market(s)

Young adults who are just starting their careers, late teens and early 20s.

Font styles to use
Sans Serif

Requirements
Must have
• Ease of use, smart and sleek, a guided setup wizard which will help users setup their account after signing up.
Should not have
• Clunky

```html
<!DOCTYPE html>
<html lang="en">
<head>
<meta charset="utf-8">
<title>Add expense</title>
<link href="https://fonts.googleapis.com/css2?family=Poppins:wght@400;600;700&display=swap" rel="stylesheet">
<style>
  :root {
    --bg: #ffffff;
    --primary: #1f7aea;
    --primary-soft: #e2edfc;
    --ink: #2a2a3c;
    --muted: #8a92a8;
    --field-border: #d5e3f6;
    --shadow: rgba(31, 122, 234, 0.35);
  }
  * { box-sizing: border-box; margin: 0; padding: 0; }
  html, body {
    width: 1200px;
    height: 2598px;
    overflow: hidden;
    background: var(--bg);
  }
  body { font-family: 'Poppins', sans-serif; color: var(--ink); }

  .screen {
    position: relative;
    width: 375px;
    height: 812px;
    transform: scale(3.2);
    transform-origin: top left;
  }

  .back-button {
    position: absolute;
    left: 16px; top: 45px;
    width: 32px; height: 32px;
    border-radius: 50%;
    background: var(--primary-soft);
    display: flex; align-items: center; justify-content: center;
  }

  .page-title {
    position: absolute;
    left: 17px; top: 158px;
    font-size: 21px;
    font-weight: 600;
    color: var(--ink);
  }

  .amount-field {
    position: absolute;
    left: 32px; top: 235px;
    width: 311px; height: 50px;
    border: 1px solid var(--field-border);
    border-radius: 10px;
    padding-left: 15px;
    display: flex; align-items: center;
    font-size: 14px;
    color: var(--muted);
  }

  .capture-option {
    position: absolute;
    left: 33px;
    width: 309px; height: 88px;
    border: 2px solid var(--primary);
    border-radius: 16px;
    display: flex; align-items: center; justify-content: center;
    gap: 8px;
    font-size: 14px;
    color: var(--ink);
  }
  .capture-option svg { flex: none; }
  .option-receipt { top: 375px; }
  .option-statement { top: 475px; }
  .option-voice { top: 575px; }

  .divider-label {
    position: absolute;
    left: 0; width: 375px; top: 689px;
    text-align: center;
    font-size: 15px;
    color: var(--ink);
  }

  .manual-button {
    position: absolute;
    left: 62px; top: 737px;
    width: 251px; height: 50px;
    border-radius: 8px;
    background: var(--primary);
    color: #ffffff;
    font-size: 13px;
    font-weight: 600;
    letter-spacing: 0.3px;
    display: flex; align-items: center; justify-content: center;
    box-shadow: 0 12px 16px -8px var(--shadow);
  }
</style>
</head>
<body>
  <main class="screen">
    <div class="back-button" aria-label="Back">
      <svg width="16" height="12" viewBox="0 0 16 12" fill="none" stroke="var(--primary)" stroke-width="2" stroke-linecap="round" stroke-linejoin="round">
        <path d="M15 6H2M6 1.5L1.5 6 6 10.5"/>
      </svg>
    </div>

    <h1 class="page-title">Add expense</h1>

    <div class="amount-field">Enter amount</div>

    <div class="capture-option option-receipt">
      <svg width="14" height="16" viewBox="0 0 14 16" fill="none" stroke="var(--primary)" stroke-width="1.6" stroke-linejoin="round" stroke-linecap="round">
        <path d="M2 1h6.5L12.5 5v9.2a.8.8 0 0 1-.8.8H2.3a.8.8 0 0 1-.8-.8V1.8A.8.8 0 0 1 2 1z"/>
        <path d="M8.5 1v4h4M4.5 8.5h5M4.5 11.5h5"/>
      </svg>
      <span>Scan receipt</span>
    </div>

    <div class="capture-option option-statement">
      <svg width="17" height="13" viewBox="0 0 17 13" fill="none" stroke="var(--primary)" stroke-width="1.6" stroke-linecap="round">
        <rect x="1" y="1" width="15" height="11" rx="1.5"/>
        <path d="M1 4.8h15M3.8 9h3"/>
      </svg>
      <span>Scan credit card statement</span>
    </div>

    <div class="capture-option option-voice">
      <svg width="14" height="17" viewBox="0 0 14 17" fill="none" stroke="var(--primary)" stroke-width="1.6" stroke-linecap="round">
        <rect x="4.5" y="1" width="5" height="9" rx="2.5" fill="var(--primary)"/>
        <path d="M1.5 7.5a5.5 5.5 0 0 0 11 0M7 13v3M4.5 16h5"/>
      </svg>
      <span>Use voice command</span>
    </div>

    <p class="divider-label">OR</p>

    <div class="manual-button">ADD INFO MANUALLY</div>
  </main>
</body>
</html>
```